Powerpoint visual improvements

I need a cover page, and our beliefs page and differentiating factors page / graphic design for our presentation. For the cover page I would just like an attractive design that incorporate our architectural concept with columns and potentially our logo. For the beliefs page I just want a more attractive presentatoin of the concepts. For the differentiating factors page I want a graphic that captures the points about how we are different from competitors. I have used the attached content to date, but I think it can be improved. The text is included in the graphic and I would also like to make sure the firm logo is incorporated.

Target Market(s)

Individual and institutional investors.

Industry/Entity Type

Investment Advisory

Requirements
Must have
• Our corporate colors are generally RGB 145,148,149; 66,68,76; 0,0,153; and 0,63,127. Our logo is attached. Our primary font is Georgia. Our website is www.PelmarCW.com. The key pages are www.PelmarCW.com/beliefs and www.PelmarCW.com/value we are trying to capture in a presentation. We also need a new presentation cover. Use the website as a reference for the type of imagery we like.

```html
<!DOCTYPE html>
<html lang="en">
<head>
<meta charset="utf-8">
<title>Cover Title Slide Ideas</title>
<link href="https://fonts.googleapis.com/css2?family=Lato:wght@300;400;700&family=Gelasio:ital,wght@0,400;0,700;1,400&display=swap" rel="stylesheet">
<style>
  :root {
    --board: #22304d;
    --band: rgba(52, 86, 138, 0.8);
    --ink-white: #ffffff;
    --ink-navy: #2c3d5e;
    --ink-dark: #1c1c1c;
    --ink-grey: #919495;
    --paper: #f7f7f7;
  }
  * { box-sizing: border-box; margin: 0; padding: 0; }
  html, body { width: 1200px; height: 1200px; overflow: hidden; }
  body { background: var(--board); font-family: "Gelasio", Georgia, serif; position: relative; }

  .board-title {
    position: absolute; top: 139px; left: 0; width: 1200px; text-align: center;
    font-family: "Lato", sans-serif; font-weight: 700; font-size: 24px;
    letter-spacing: 0.3px; color: var(--ink-white);
  }

  .slide {
    position: absolute; width: 320px; height: 180px; overflow: hidden;
    box-shadow: 0 4px 8px rgba(0,0,0,0.45);
  }
  .photo { position: absolute; left: 0; top: 0; width: 100%; height: 100%; }

  /* Soft tonal fills standing in for the column photography */
  .photo--hall-wood {
    background:
      linear-gradient(90deg, rgba(200,205,212,0) 0%, rgba(200,205,212,0.18) 18%, rgba(200,205,212,0) 32%, rgba(200,205,212,0.2) 58%, rgba(200,205,212,0) 72%, rgba(220,224,230,0.3) 86%, rgba(200,205,212,0) 100%),
      linear-gradient(180deg, #8a8f96 0%, #6c6a66 30%, #6a5642 55%, #5a4634 80%, #4c3b2d 100%);
  }
  .photo--colonnade {
    background:
      linear-gradient(90deg, rgba(230,225,214,0.35) 0%, rgba(230,225,214,0.05) 25%, rgba(0,0,0,0.08) 50%, rgba(230,225,214,0.05) 75%, rgba(230,225,214,0.3) 100%),
      linear-gradient(180deg, #a29d92 0%, #86837c 40%, #6b6b69 70%, #5a5c5e 100%);
  }
  .photo--fluted {
    background:
      radial-gradient(ellipse 40% 80% at 22% 45%, rgba(214,200,170,0.55) 0%, rgba(214,200,170,0) 100%),
      radial-gradient(ellipse 30% 60% at 52% 40%, rgba(200,186,156,0.4) 0%, rgba(200,186,156,0) 100%),
      linear-gradient(100deg, #8a7d66 0%, #6e6552 40%, #55503f 75%, #45423a 100%);
  }
  .photo--blue {
    height: 121px;
    background:
      linear-gradient(90deg, rgba(120,150,196,0) 0%, rgba(120,150,196,0.22) 10%, rgba(120,150,196,0) 20%, rgba(120,150,196,0.22) 30%, rgba(120,150,196,0) 42%, rgba(120,150,196,0.25) 60%, rgba(120,150,196,0) 72%, rgba(130,160,205,0.32) 88%, rgba(120,150,196,0) 100%),
      linear-gradient(180deg, #3f5478 0%, #34486b 45%, #2e4163 100%);
  }
  .photo--dark {
    background:
      radial-gradient(ellipse 30% 70% at 18% 55%, rgba(120,118,110,0.45) 0%, rgba(120,118,110,0) 100%),
      radial-gradient(ellipse 22% 55% at 50% 50%, rgba(120,118,110,0.35) 0%, rgba(120,118,110,0) 100%),
      linear-gradient(100deg, #4b4a46 0%, #3e3e3b 50%, #333536 100%);
  }

  .paper { position: absolute; left: 0; top: 121px; width: 100%; height: 59px; background: var(--paper); }
  .band { position: absolute; left: 0; width: 100%; height: 31px; background: var(--band); }

  .brand {
    position: absolute; display: flex; align-items: center; gap: 4px;
    transform: translate(-50%, -50%);
    font-family: "Lato", sans-serif; font-weight: 300; color: var(--ink-white);
  }
  .brand-dot { width: 36px; height: 36px; border-radius: 50%; background: currentColor; }
  .brand-name { font-size: 17px; line-height: 1; }
  .brand--left { transform: translate(0, -50%); }
  .brand--grey { color: var(--ink-grey); }
  .brand--grey .brand-dot { width: 46px; height: 46px; }
  .brand--grey .brand-name { font-size: 22px; }

  .tagline {
    position: absolute; left: 0; width: 100%; text-align: center;
    font-style: italic; font-size: 5.6px; color: var(--ink-white);
  }
  .tagline--navy { color: var(--ink-navy); }
  .blurb {
    position: absolute; left: 50%; transform: translateX(-50%); width: 130px;
    text-align: center; font-size: 3.2px; line-height: 5.4px; color: rgba(255,255,255,0.85);
  }
  .blurb--navy { color: #5d6470; }
  .rule { position: absolute; left: 78px; width: 164px; height: 0.6px; background: #8c93a0; }

  .pres-title { position: absolute; font-weight: 700; font-size: 12px; letter-spacing: 0.2px; color: var(--ink-dark); white-space: nowrap; }
  .pres-title--light { font-weight: 400; color: var(--ink-white); }
  .pres-date { position: absolute; font-size: 4.4px; color: var(--ink-dark); white-space: nowrap; }
  .pres-date--light { color: var(--ink-white); }
</style>
</head>
<body>
  <h1 class="board-title">COVER TITLE&nbsp; SLIDE IDEAS</h1>

  <section class="slide" style="left:71px; top:295px;">
    <div class="photo photo--hall-wood" role="img" aria-label="Photo of a hall with pale columns reflected on a polished wooden floor"></div>
    <div class="band" style="top:32px;"></div>
    <div class="brand" style="left:160px; top:48px;"><span class="brand-dot"></span><span class="brand-name">Pelmar</span></div>
    <p class="tagline" style="top:105px;">Pelmar Capital Wealth is an investment advisor founded by investors.</p>
    <p class="blurb" style="top:117px;">We aim to raise the long term value of your portfolio by cutting costs, using our research platform and clear portfolio design.</p>
  </section>

  <section class="slide" style="left:446px; top:295px;">
    <div class="photo photo--colonnade" role="img" aria-label="Photo of a stone colonnade walkway with columns casting shadows"></div>
    <div class="band" style="top:101px;"></div>
    <div class="brand" style="left:160px; top:117px;"><span class="brand-dot"></span><span class="brand-name">Pelmar</span></div>
    <p class="tagline" style="top:145px;">Pelmar Capital Wealth is an investment advisor founded by investors.</p>
    <p class="blurb" style="top:160px;">We aim to raise the long term value of your portfolio by cutting costs, using our research platform and clear portfolio design.</p>
  </section>

  <section class="slide" style="left:820px; top:295px;">
    <div class="photo photo--fluted" role="img" aria-label="Photo of a row of fluted classical columns on a wet reflective floor"></div>
    <div class="band" style="top:16px;"></div>
    <div class="brand brand--left" style="left:6px; top:32px;"><span class="brand-dot"></span><span class="brand-name">Pelmar</span></div>
    <p class="tagline" style="top:145px;">Pelmar Capital Wealth is an investment advisor founded by investors.</p>
    <p class="blurb" style="top:160px;">We aim to raise the long term value of your portfolio by cutting costs, using our research platform and clear portfolio design.</p>
  </section>

  <section class="slide" style="left:71px; top:502px;">
    <div class="paper"></div>
    <div class="photo photo--blue" role="img" aria-label="Blue-tinted photo of columns reflected on a glossy floor"></div>
    <div class="brand" style="left:160px; top:63px;"><span class="brand-dot"></span><span class="brand-name">Pelmar</span></div>
    <p class="tagline tagline--navy" style="top:134px;">Pelmar Capital Wealth is an investment advisor founded by investors.</p>
    <div class="rule" style="top:144px;"></div>
    <p class="blurb blurb--navy" style="top:149px;">We aim to raise the long term value of your portfolio by cutting costs, using our research platform and clear portfolio design.</p>
  </section>

  <section class="slide" style="left:446px; top:502px;">
    <div class="paper"></div>
    <div class="photo photo--blue" role="img" aria-label="Blue-tinted photo of columns reflected on a glossy floor"></div>
    <div class="brand" style="left:160px; top:63px;"><span class="brand-dot"></span><span class="brand-name">Pelmar</span></div>
    <h2 class="pres-title" style="left:0; width:100%; text-align:center; top:133px;">PRESENTATION TITLE</h2>
    <p class="pres-date" style="left:0; width:100%; text-align:center; top:153px;">May 25th, 2018</p>
  </section>

  <section class="slide" style="left:820px; top:502px;">
    <div class="paper"></div>
    <div class="photo photo--blue" role="img" aria-label="Blue-tinted photo of columns reflected on a glossy floor"></div>
    <p class="tagline" style="top:51px;">Pelmar Capital Wealth is an investment advisor founded by investors.</p>
    <p class="blurb" style="top:66px;">We aim to raise the long term value of your portfolio by cutting costs, using our research platform and clear portfolio design.</p>
    <div class="brand brand--grey" style="left:160px; top:150px;"><span class="brand-dot"></span><span class="brand-name">Pelmar</span></div>
  </section>

  <section class="slide" style="left:446px; top:713px;">
    <div class="photo photo--dark" role="img" aria-label="Darkened photo of fluted classical columns on a reflective floor"></div>
    <div class="band" style="top:28px;"></div>
    <div class="brand brand--left" style="left:203px; top:44px;"><span class="brand-dot"></span><span class="brand-name">Pelmar</span></div>
    <h2 class="pres-title pres-title--light" style="left:29px; top:136px;">PRESENTATION TITLE</h2>
    <p class="pres-date pres-date--light" style="left:0; width:190px; text-align:center; top:154px;">May 25th, 2018</p>
  </section>
</body>
</html>
```